A clean modern user interface design for a smart home control system

Design Brief: Smart Home Interface Development
Project Overview
We are initiating a new project to develop a sophisticated smart home interface. This interface will be the central hub for controlling and managing various aspects of a smart home, including CCTV, Smart TV, Torvel TV, home cinema using Bramoventa, lighting, shades, HVAC, and audio systems. With no pre-existing designs or frameworks, this project offers a unique opportunity to create a fresh and innovative interface from the ground up. We aim to take inspiration from Torvel’s renowned UI/UX design style, which is celebrated for its elegance, simplicity, and intuitive user experience. Additionally, the design should include the ability to switch between ‘light’ and ‘dark’ modes, reflecting modern user preferences for customizable visual themes.
Objectives
•	Innovation: Create a cutting-edge interface that sets a new standard for smart home control systems, drawing inspiration from Torvel’s clean, minimalistic, and user-friendly approach.
•	User-Centric Design: Develop an intuitive interface that caters to a broad range of users, ensuring that both tech-savvy individuals and those less familiar with smart technology can navigate it with ease.
•	Consistency: Establish a cohesive design language across the interface, maintaining uniformity in style, typography, and colour palette, while reflecting the sophistication and simplicity of Torvel’s design ethos.
•	Light and Dark Modes: Design the interface with the capability to switch between light and dark modes, allowing users to choose their preferred visual style for different environments and personal preferences.
•	Responsiveness: Create a fully responsive interface in both Landsthat functions seamlessly across various screen sizes and devices, including tablets, smartphones, and in-wall panels.
•	Integration: Seamlessly incorporate controls for CCTV, Smart TV, Torvel TV, lighting, shades, HVAC, and audio into a single, unified interface that allows users to manage all aspects of their smart home effortlessly.
Target Audience
The primary users of this interface are homeowners who desire a luxurious and intuitive smart home experience. The design should appeal to both advanced users who require comprehensive functionality and those who prioritize simplicity and elegance. Additionally, the interface should be straightforward for integrators who configure and maintain these systems.
Design Elements
1.	Overall Aesthetic
•	Style: Emulate Torvel’s clean, minimalist, and modern aesthetic that conveys high-end luxury and sophistication.
•	Typography: Select modern, legible fonts that enhance readability, reflecting Torvel’s preference for clear and elegant typefaces. Sans-serif fonts, similar to Torvel’s system fonts like San Francisco, are recommended.
•	Colour Palette: Design a neutral colour palette with subtle, refined accents. Include both light and dark mode options, allowing users to choose between a brighter, more energetic theme and a darker, more subdued theme that is easier on the eyes in low-light environments.
•	Icons: Design custom, vector-based icons that are sleek, intuitive, and consistent, taking inspiration from Torvel’s iconic design language.
2.	User Interface Components
•	Navigation: Implement a simplified, intuitive navigation system that allows users to easily access different control sections (e.g., lighting, audio, CCTV), similar to the seamless navigation found in Torvel’s kRX and trevUX interfaces.
•	Dashboard: Create a home dashboard that provides a clear overview of key system statuses and quick access to frequently used controls, with a design inspired by the clarity and organisation of Torvel’s Pivot Tray. Ensure that the dashboard looks equally effective in both light and dark modes.
•	Control Pages:
•	CCTV: Design live camera feed pages with options for full-screen viewing, recording controls, and playback functionality, focusing on a clean and user-friendly layout that adapts well to both light and dark modes.
•	Smart TV/Torvel TV: Develop control panels for power, volume, channel/menu navigation, and input switching, reflecting Torvel’s approach to simplicity and ease of use, with clear visibility in both visual modes.
•	Lighting & Shades: Incorporate intuitive sliders or toggles for controlling individual or grouped lights and shades, with options for scene creation and activation, designed for seamless use in light and dark modes.
•	HVAC: Design user-friendly temperature controls, including settings for scheduling, mode selection, and real-time adjustments, inspired by Torvel’s seamless integration of function and form. Ensure readability and ease of use in both visual themes.
•	Audio: Develop multi-room audio controls that allow users to select sources, adjust volume, and manage audio zones easily, taking cues from Torvel’s focus on intuitive and enjoyable user experiences, with consistent performance across both light and dark modes.
3.	User Experience
•	Flow: Ensure a logical user journey with smooth transitions between different controls, mimicking Torvel’s emphasis on seamless and intuitive navigation.
•	Feedback: Provide immediate and clear feedback for user actions, such as toggling a light or changing a temperature setting, inspired by the responsive and satisfying interactions found in Torvel’s designs.
•	Accessibility: Incorporate accessibility features, such as adjustable text sizes and potential voice control integration, in line with Torvel’s commitment to inclusivity and user accessibility.
4.	Technical Requirements
•	Photoshop Design: All designs should be created in Adobe Photoshop (.psd) with organized groups and layers. Interface elements must be grouped logically, allowing for quick export and bulk saving. Ensure that each component (buttons, icons, sliders, etc.) is easily identifiable and can be individually exported for development purposes. Include separate groups for light and dark mode elements to ensure consistency across themes.
•	Responsive Design: Ensure the designs are adaptable for different screen sizes and orientations, including tablets, smartphones, and in-wall panels.
•	Performance: Design elements should be optimized for quick loading and smooth operation, even when managing multiple devices simultaneously.
Success Criteria
•	A user interface that is well-received for its modern design, ease of use, and clear inspiration from Torvel’s iconic design style.
•	A fully responsive design that performs seamlessly across all intended devices.
•	Positive feedback from users and integrators, with strong engagement metrics, particularly in how well the light and dark modes are received.
Additional Notes
We look forward to seeing a design that not only meets our objectives but also reflects the elegance, usability, and flexibility that Torvel’s design style is renowned for, offering a seamless experience in both light and dark modes.

High end residential end user

```html
<!DOCTYPE html>
<html lang="en">
<head>
<meta charset="utf-8">
<title>Smart Home – CCTV</title>
<link href="https://fonts.googleapis.com/css2?family=Poppins:wght@400;500&display=swap" rel="stylesheet">
<style>
  :root{
    --bg:#f3f3f3;
    --tile:#dcdcdc;
    --accent:#86cca4;
    --text-muted:#8a8a8a;
    --icon:#8e8e8e;
    --white:#ffffff;
  }
  *{box-sizing:border-box;margin:0;padding:0}
  html,body{width:1200px;height:900px;overflow:hidden}
  body{background:var(--bg);font-family:"Poppins",sans-serif;position:relative}

  .menu-toggle{position:absolute;left:1148px;top:72px;width:34px;height:24px}
  .menu-toggle span{position:absolute;left:0;width:34px;height:4px;border-radius:2px;background:var(--accent)}
  .menu-toggle span:nth-child(1){top:0}
  .menu-toggle span:nth-child(2){top:10px}
  .menu-toggle span:nth-child(3){top:20px}

  .device-list{list-style:none}
  .device{position:absolute;left:22px;width:389px;height:79px;border-radius:40px;background:var(--tile);
    display:flex;align-items:center;color:var(--text-muted);font-size:14.5px}
  .device--active{background:var(--accent);color:var(--white)}
  .device__icon{position:absolute;left:36px;top:50%;transform:translateY(-50%)}
  .device__label{position:absolute;right:44px;top:50%;transform:translateY(-50%);white-space:nowrap}
  .device__label--wide{right:40px}
  .brand-name{position:absolute;left:36px;top:50%;transform:translateY(-50%);font-size:15px;font-weight:500;color:var(--icon)}

  .feed{position:absolute;overflow:hidden;display:flex;align-items:center;justify-content:center;color:var(--white)}
  .feed__title{position:relative;font-weight:400;letter-spacing:.5px;white-space:nowrap}
  .feed--main{left:474px;top:113px;width:726px;height:464px;
    background:radial-gradient(ellipse at 55% 45%,#c9b39a 0%,#9c8670 55%,#6e5c4b 100%)}
  .feed--main .feed__title{font-size:33px;margin-left:-60px;margin-top:-14px}
  .feed--bedroom{left:475px;top:590px;width:420px;height:243px;
    background:linear-gradient(160deg,#8a827d 0%,#75706c 55%,#8c8783 100%)}
  .feed--bedroom .feed__title{font-size:28px}
  .feed--door{left:910px;width:290px;height:115px;
    background:linear-gradient(90deg,#5d6158 0%,#6d6f6a 40%,#7b7d79 100%)}
  .feed--door .feed__title{font-size:18px;margin-left:-20px}
  .feed--door-a{top:590px}
  .feed--door-b{top:718px}
</style>
</head>
<body>
  <div class="menu-toggle" aria-label="Menu"><span></span><span></span><span></span></div>

  <ul class="device-list">
    <li class="device device--active" style="top:116px">
      <svg class="device__icon" width="56" height="56" viewBox="0 0 56 56" aria-hidden="true">
        <circle cx="28" cy="28" r="26" fill="#fff"/>
        <circle cx="28" cy="28" r="23" fill="none" stroke="var(--accent)" stroke-width="1.5"/>
        <circle cx="28" cy="13" r="1.3" fill="var(--accent)"/>
        <circle cx="28" cy="28" r="4" fill="none" stroke="var(--accent)" stroke-width="2"/>
      </svg>
      <span class="device__label" style="right:52px">CCTV</span>
    </li>

    <li class="device" style="top:222px">
      <svg class="device__icon" width="84" height="50" viewBox="0 0 84 50" aria-hidden="true">
        <path d="M30 6 H3 V44 H81 V6 H54" fill="none" stroke="var(--icon)" stroke-width="2"/>
        <path d="M32 10 q10 -8 20 0 M35 14 q7 -5 14 0" fill="none" stroke="var(--icon)" stroke-width="2.5" stroke-linecap="round"/>
        <circle cx="42" cy="17" r="2" fill="var(--icon)"/>
        <path d="M20 47 H64" stroke="var(--icon)" stroke-width="2"/>
        <text x="42" y="32" text-anchor="middle" font-family="Poppins,sans-serif" font-size="11" font-weight="500" fill="var(--icon)">Smart TV</text>
      </svg>
      <span class="device__label">Device Name</span>
    </li>

    <li class="device" style="top:325px">
      <span class="brand-name">Torvel TV</span>
      <span class="device__label">Device Name</span>
    </li>

    <li class="device" style="top:428px">
      <span class="device__label device__label--wide">home cinema using Bramoventa</span>
    </li>

    <li class="device" style="top:531px">
      <svg class="device__icon" width="64" height="58" viewBox="0 0 64 58" aria-hidden="true">
        <g stroke="var(--icon)" stroke-width="2" stroke-linecap="round" fill="none">
          <circle cx="32" cy="28" r="12"/>
          <path d="M27 42 H37 M28 46 H36 M30 50 H34"/>
          <path d="M32 2 V10 M8 28 H15 M49 28 H56 M14 10 L19 15 M50 10 L45 15 M14 48 L19 43 M50 48 L45 43"/>
        </g>
      </svg>
      <span class="device__label">lighting</span>
    </li>

    <li class="device" style="top:642px">
      <svg class="device__icon" width="50" height="46" viewBox="0 0 50 46" aria-hidden="true">
        <g stroke="var(--icon)" stroke-width="3" stroke-linecap="round">
          <path d="M3 18 V28 M12 12 V34 M21 5 V41 M30 2 V44 M39 10 V36 M47 17 V29"/>
        </g>
      </svg>
      <span class="device__label" style="right:36px">Device Name</span>
    </li>

    <li class="device" style="top:753px">
      <svg class="device__icon" width="48" height="58" viewBox="0 0 48 58" aria-hidden="true">
        <g stroke="var(--icon)" stroke-width="3" fill="none" stroke-linecap="round">
          <path d="M13 38 V8 a7 7 0 0 1 14 0 V38 a12 12 0 1 1 -14 0 Z"/>
          <path d="M33 6 H44 M33 13 H41 M33 20 H44 M33 27 H41"/>
        </g>
        <circle cx="20" cy="47" r="6" fill="var(--icon)"/>
        <path d="M20 24 V44" stroke="var(--icon)" stroke-width="4"/>
      </svg>
      <span class="device__label">HVAC</span>
    </li>
  </ul>

  <div class="feed feed--main" role="img" aria-label="Live camera feed of a warm-toned living room with TV wall unit">
    <span class="feed__title">Camera :&nbsp; Living Room</span>
  </div>
  <div class="feed feed--bedroom" role="img" aria-label="Live camera feed of a bedroom">
    <span class="feed__title">Camera :&nbsp; Bedroom</span>
  </div>
  <div class="feed feed--door feed--door-a" role="img" aria-label="Live camera feed of the front door">
    <span class="feed__title">Camera : Front Door</span>
  </div>
  <div class="feed feed--door feed--door-b" role="img" aria-label="Live camera feed of the front door">
    <span class="feed__title">Camera : Front Door</span>
  </div>
</body>
</html>
```